Design for Card Attached to Clothes

We sell rhythmic gymnastics apparel and are looking for someone create a card that will be attached to the products. You can see an example of the exact type of apparel in the files, as well as the current card that is attached to it. The design should have space on the top back for the sticker that has UPC and SKU information, as shown in the image attached.
- We would like the front to have our logo
- We would like the image of the girls added on the back
- Would be cool to see the gradient change to the white space on the back where the sticker will go but not required.
-The final card size is 10cm by 6cm, Their should be 2mm loss accounted for cutting the cards within the design. (meaning the design needs to be bigger than 10cm by 6cm to account for printing and cut)
- And the hole size that is at the top center is 3mm in diameter
- Name should be under logo
Access all logo files here https://files.brimvale.net/share/47Qk2pxTzWm9LcR8vNd3HyJb6sEa1Uo?view=open
- Front will have logo
- Back will have image of girls and some creative design that you will create.
Females
Rhythmic Gymnastics

```html
<!DOCTYPE html>
<html lang="en">
<head>
<meta charset="utf-8">
<title>Velvira Hang Tag – Front and Back</title>
<link href="https://fonts.googleapis.com/css2?family=Quicksand:wght@500&family=Dancing+Script:wght@600&display=swap" rel="stylesheet">
<style>
  :root {
    --backdrop: #cbcbcb;
    --card: #ffffff;
    --brand-pink: #e80c7c;
    --band-pink: #d3198a;
    --ink: #1b1b1b;
    --hole-dark: #3a3a40;
    --photo-top: rgba(120, 70, 100, 0.18);
    --photo-bottom: rgba(55, 35, 50, 0.55);
  }
  * { margin: 0; padding: 0; box-sizing: border-box; }
  html, body {
    width: 1200px;
    height: 1000px;
    overflow: hidden;
    background: var(--backdrop);
  }
  .stage {
    position: relative;
    width: 1200px;
    height: 1000px;
  }
  .tag {
    position: absolute;
    top: 225px;
    width: 354px;
    height: 590px;
    background: var(--card);
    box-shadow: 0 2px 8px rgba(0,0,0,0.45);
    overflow: hidden;
  }
  .tag--front { left: 157px; }
  .tag--back { left: 677px; }

  .tag__hole {
    position: absolute;
    left: 50%;
    top: 60px;
    width: 17px;
    height: 17px;
    margin-left: -8.5px;
    border-radius: 50%;
    z-index: 3;
  }
  .tag--front .tag__hole { background: var(--card); }
  .tag--back .tag__hole { background: var(--hole-dark); }

  .front__band {
    position: absolute;
    left: 0; top: 0;
    width: 100%;
    height: 162px;
    background: linear-gradient(to bottom, var(--band-pink) 0%, rgba(211,25,138,0.55) 55%, rgba(211,25,138,0) 100%);
  }
  .brand {
    position: absolute;
    left: 0;
    top: 210px;
    width: 100%;
    display: flex;
    flex-direction: column;
    align-items: center;
  }
  .brand__dot {
    width: 176px;
    height: 176px;
    border-radius: 50%;
    background: var(--brand-pink);
  }
  .brand__name {
    margin-top: 8px;
    font-family: "Quicksand", sans-serif;
    font-weight: 500;
    font-size: 50px;
    line-height: 1;
    color: var(--brand-pink);
  }
  .tagline {
    position: absolute;
    left: 0;
    top: 520px;
    width: 100%;
    text-align: center;
    font-family: "Dancing Script", cursive;
    font-weight: 600;
    font-size: 27px;
    color: var(--ink);
  }

  .back__band {
    position: absolute;
    left: 0; bottom: 0;
    width: 100%;
    height: 300px;
    background: linear-gradient(to top, var(--band-pink) 0%, rgba(211,25,138,0.55) 55%, rgba(211,25,138,0) 100%);
  }
  .back__photo {
    position: absolute;
    left: 6px;
    top: 312px;
    width: 342px;
    height: 272px;
    border-radius: 8px;
    background: linear-gradient(to bottom, var(--photo-top) 0%, var(--photo-bottom) 100%);
  }
</style>
</head>
<body>
  <main class="stage">
    <section class="tag tag--front" aria-label="Tag front">
      <div class="front__band"></div>
      <span class="tag__hole"></span>
      <div class="brand">
        <span class="brand__dot"></span>
        <span class="brand__name">Velvira</span>
      </div>
      <p class="tagline">We Got You Covered</p>
    </section>

    <section class="tag tag--back" aria-label="Tag back">
      <span class="tag__hole"></span>
      <div class="back__band"></div>
      <div class="back__photo" role="img" aria-label="Photo of two rhythmic gymnasts in black leotards stretching on the floor with arms raised"></div>
    </section>
  </main>
</body>
</html>
```